Domain Search Page and Results

We are looking for creative methods to display a domain registration search page, with many extensions. We are only looking for designs of the inside of the page and not for the frame around the page.
There are currently 4 categories and after pressing submit there is the results: however in the future there will be more categories (around 7 or 8) and domain extensions.
We would like creative methods to display the different (7-8) categories and extensions and also the results display.
The categories should be open/close-able.
We are planning to use JQuery and your suggestions for any movement will be appreciated.
We also would like creative ways to display the results.
Thank you.
Additions:
- It is not necessary to change the template/frame of the page. We are only looking for the search AND results display.
- We are looking for creative ideas and not necessary judging based on the actual design.
- We are basing the winner on how creatively it will be possible to display the search function AND results display. And to display creatively 7 or 8 categories with 100''s of domain extensions. The more creative and yet still user friendly the search functionality is, the chances of being selected will be higher.
- There will be 7 or 8 categories (and not just 4 as in the sample). The design must be able to extend to 7 or 8 categories. In some categories there are over 100 extensions. Creative ideas on how to sub categorize the extensions will be a bonus.

```html
<!DOCTYPE html>
<html lang="en">
<head>
<meta charset="utf-8">
<title>Domain Search Availability</title>
<link rel="stylesheet" href="https://fonts.googleapis.com/css2?family=Mulish:wght@300;400;600;700&display=swap">
<style>
:root{
  --red:#cc1419;
  --red-dark:#b00d12;
  --cyan:#37b4ea;
  --cyan-light:#6fdcf8;
  --text:#555;
  --muted:#8a8a8a;
  --line:#dcdcdc;
  --panel:#f4f4f4;
  --footer:#ececec;
}
*{box-sizing:border-box;margin:0;padding:0}
html,body{width:854px;height:1200px;overflow:hidden;background:#fff}
body{position:relative;font-family:"Mulish",sans-serif;color:var(--text)}
.abs{position:absolute}
.account-links{right:58px;top:11px;font-size:11px;color:#777}
.brand{left:54px;top:34px;display:flex;align-items:center;gap:10px}
.brand-mark{width:48px;height:48px;border-radius:50%;background:var(--red)}
.brand-name{font-size:22px;font-weight:700;color:#222}
.lang-select{left:715px;top:68px;width:83px;height:24px;border:1px solid #ccc;border-radius:2px;font-size:10.5px;display:flex;align-items:center;padding-left:9px;gap:6px;color:#333}
.lang-flag{width:16px;height:11px;background:#2b3f8c}
.lang-caret{width:0;height:0;border-left:4px solid transparent;border-right:4px solid transparent;border-top:5px solid #555;margin-left:4px}
.main-nav{left:51px;top:105px;width:753px;height:40px;background:linear-gradient(#35b4ee,#2a9fe0);display:flex;color:#fff;font-size:13px;font-weight:600}
.main-nav a{height:40px;display:flex;align-items:center;justify-content:center;border-right:1px solid rgba(255,255,255,.35);color:#fff;text-decoration:none}
.main-nav .control-panel{margin-left:auto;width:121px;background:var(--cyan-light);border:0;font-weight:400}
.hero{left:51px;top:145px;width:753px;height:152px;background:linear-gradient(90deg,#3a4a63 0%,#6e7b8e 35%,#e8c232 52%,#e6e6e6 70%,#6d7480 100%)}
.page-title{left:50px;top:320px;font-size:19px;font-weight:400;color:var(--red)}
.intro{left:51px;top:350px;width:740px;font-size:9.6px;line-height:16px;font-weight:300}
.field-label{left:52px;top:427px;font-size:13px;color:#555}
.domain-input{left:52px;top:449px;width:369px;height:31px;border:1px solid #ccc;background:#f5f5f5;font-size:9.5px;color:#999;padding:11px 13px}
.category{left:51px;top:516px;width:753px;height:121px;border:1px solid var(--line);border-bottom:0;background:linear-gradient(#fff 60%,#f3f3f3)}
.category-head{height:38px;background:var(--panel);border-bottom:1px solid var(--line);font-size:13px;color:#444;padding:12px 16px;position:relative}
.category-close{position:absolute;right:15px;top:12px}
.ext-grid{position:relative}
.ext{position:absolute;font-size:9.5px;color:#666;display:flex;align-items:center;gap:7px}
.ext i{width:12px;height:12px;border:1px solid #bbb;background:#fff}
.accordion{left:51px;width:753px;height:35px;background:linear-gradient(var(--red),var(--red-dark));color:#fff;font-size:13.5px;font-weight:600;padding:9px 14px;border-top:1px solid #d9383c}
.accordion svg{position:absolute;right:16px;top:13px}
.btn{background:linear-gradient(#5ccaf5,var(--cyan));color:#fff;font-size:12.5px;font-weight:600;display:flex;align-items:center;justify-content:center}
.results-title{left:52px;top:832px;font-size:12.5px;color:var(--red)}
.results{left:51px;top:863px;width:412px;border:1px solid #e2e2e2;border-collapse:collapse;font-size:9.5px;color:#777}
.results th{height:32px;background:#efefef;font-weight:400;font-size:12px;color:#555;text-align:left;padding-left:21px}
.results th:nth-child(2){padding-left:29px}
.results th:nth-child(3){text-align:center;padding-left:0}
.results td{height:22px;border-top:1px solid #e6e6e6;padding-left:21px}
.results td:nth-child(2){padding-left:29px}
.results td:nth-child(3){text-align:left;padding-left:46px;vertical-align:top;padding-top:3px}
.results th+th,.results td+td{border-left:1px solid #e2e2e2}
.results td:first-child{width:184px}
.results td:nth-child(2){width:110px}
.tick-box{display:inline-block;width:12px;height:11px;border:1px solid #ccc}
.results tr:last-child td{height:29px;vertical-align:top;padding-top:4px}
.site-footer{left:0;top:1153px;width:854px;height:47px;background:var(--footer)}
.copyright{position:absolute;left:50px;top:18px;font-size:9.6px;color:#666}
.social{position:absolute;left:735px;top:14px;display:flex;gap:6px}
.social i{width:18px;height:18px;border-radius:50%;background:#555}
</style>
</head>
<body>
<div class="abs account-links">Login &nbsp;/&nbsp; Create Account</div>
<div class="abs brand"><span class="brand-mark"></span><span class="brand-name">Kumo Domains</span></div>
<div class="abs lang-select"><span class="lang-flag"></span>English<span class="lang-caret"></span></div>

<nav class="abs main-nav">
  <a style="width:80px">Home</a><a style="width:73px">Pricing</a><a style="width:71px">Search</a><a style="width:59px">FAQ</a><a style="width:130px">Hosting in Japan</a><a style="width:86px">Resellers</a><a style="width:75px;border:0">Contact us</a>
  <a class="control-panel">Control Panel</a>
</nav>

<div class="abs hero" role="img" aria-label="Banner photo of a hand writing a www dot com web address on a board"></div>

<h1 class="abs page-title">Domain Search Availability</h1>
<p class="abs intro">Mauris vel lacus vitae felis vestibulum volutpat Etiam est nunc venenatis in tristique eu imperdiet ac nisl Cum sociis natoque penatibus et magnis dis parturient montes nascetur ridiculus mus In iaculis facilisis massa Etiam eu urna Sed porta Suspendisse quam leo molestie sed luctus quis feugiat in pede Fusce tellus Sed metus augue convallis et vehicula ut pulvinar eu ante Integer orci tellus tristique vitae consequat</p>

<div class="abs field-label">Enter Domain Below</div>
<div class="abs domain-input">type your domain here</div>

<section class="abs category">
  <div class="category-head">Japan Domain
    <svg class="category-close" width="13" height="13" viewBox="0 0 13 13"><path d="M1 1L12 12M12 1L1 12" stroke="#999" stroke-width="2.4"/></svg>
  </div>
  <div class="ext-grid">
    <span class="ext" style="left:20px;top:21px"><i></i>.jp</span>
    <span class="ext" style="left:119px;top:21px"><i></i>ne.jp</span>
    <span class="ext" style="left:217px;top:21px"><i></i>co.jp</span>
    <span class="ext" style="left:316px;top:21px"><i></i>gr.jp</span>
    <span class="ext" style="left:20px;top:46px"><i></i>tokyo.jp</span>
    <span class="ext" style="left:119px;top:46px"><i></i>osaka.jp</span>
    <span class="ext" style="left:217px;top:46px"><i></i>kyoto.jp</span>
  </div>
</section>

<div class="abs accordion" style="top:637px">Japan Regional Domains<svg width="18" height="9" viewBox="0 0 18 9"><path d="M1 1L9 8L17 1" fill="none" stroke="#fff" stroke-width="1.3"/></svg></div>
<div class="abs accordion" style="top:672px">gTDL Domains<svg width="18" height="9" viewBox="0 0 18 9"><path d="M1 1L9 8L17 1" fill="none" stroke="#fff" stroke-width="1.3"/></svg></div>
<div class="abs accordion" style="top:707px;height:37px">ccTDL Domains<svg width="18" height="9" viewBox="0 0 18 9"><path d="M1 1L9 8L17 1" fill="none" stroke="#fff" stroke-width="1.3"/></svg></div>

<div class="abs btn" style="left:50px;top:759px;width:104px;height:32px">Search Here</div>

<div class="abs results-title">Results shown here after pressing search:</div>
<table class="abs results">
  <tr><th>Domain</th><th>Results</th><th>Check</th></tr>
  <tr><td>dsafsdred.jp</td><td>Available</td><td><span class="tick-box"></span></td></tr>
  <tr><td>dsafsdred.com</td><td>Available</td><td><span class="tick-box"></span></td></tr>
  <tr><td>dsafsdred.net</td><td>Available</td><td><span class="tick-box"></span></td></tr>
  <tr><td>dsafsdred.org</td><td>Available</td><td><span class="tick-box"></span></td></tr>
  <tr><td>dsafsdred.club</td><td>Available</td><td><span class="tick-box"></span></td></tr>
  <tr><td>dsafsdred.in</td><td>Available</td><td><span class="tick-box"></span></td></tr>
  <tr><td>dsafsdred.tw</td><td>Available</td><td><span class="tick-box"></span></td></tr>
  <tr><td>dsafsdred.co</td><td>Available</td><td><span class="tick-box"></span></td></tr>
</table>

<div class="abs btn" style="left:47px;top:1098px;width:136px;height:32px">Domain Purchase</div>

<footer class="abs site-footer">
  <div class="copyright">© 2013 Company Name.&nbsp; All right reserved.&nbsp; Term of Use</div>
  <div class="social"><i></i><i></i><i></i></div>
</footer>
</body>
</html>
```